Business card for plumber

I need a business card for my plumbing company.
on it should:
Surname
position
E-mail
Telephone & mobile phone
Website
Please everything as placeholders / fantasy names.
We stand for high quality, hygiene and professionalism.

Colours:
# 606060 anthracite
# f7931e orange
# 2b89cc blue

Industry/Entity Type

Plumber

Contact Information for Business Card

folgt...

```html
<!DOCTYPE html>
<html lang="en">
<head>
<meta charset="utf-8">
<title>Brunnfeld Haustechnik – Business Card</title>
<link rel="stylesheet" href="https://fonts.googleapis.com/css2?family=Montserrat:wght@600;700;800&family=Roboto:wght@400;500&display=swap">
<style>
  :root {
    --anthracite: #606060;
    --anthracite-dark: #555555;
    --orange: #f7931e;
    --blue: #2b89cc;
    --white: #ffffff;
    --ink: #4a4a4a;
    --backdrop: #e6e6e6;
  }
  * { margin: 0; padding: 0; box-sizing: border-box; }
  html, body { width: 1200px; height: 900px; overflow: hidden; }
  body {
    background: var(--backdrop);
    display: flex; flex-direction: column; align-items: center; justify-content: center;
    gap: 40px;
    font-family: "Roboto", Arial, sans-serif;
  }
  .card {
    position: relative;
    width: 680px; height: 389px;
    border-radius: 22px;
    overflow: hidden;
    box-shadow: 0 6px 18px rgba(0,0,0,.18);
  }

  /* Back side */
  .card-back { background: var(--anthracite); }
  .card-back .pattern-area {
    position: absolute; inset: 0;
    background: linear-gradient(135deg, #676767 0%, #5c5c5c 55%, #626262 100%);
  }
  .card-back .back-brand {
    position: absolute; right: 60px; bottom: 150px;
    display: flex; align-items: center; gap: 8px;
    font-family: "Montserrat", Arial, sans-serif; font-weight: 700;
    font-size: 13px; letter-spacing: .5px; color: var(--white);
  }
  .brand-dot { width: 12px; height: 12px; border-radius: 50%; background: var(--orange); flex: none; }

  /* Front side */
  .card-front { background: var(--white); }
  .brand {
    position: absolute; left: 36px; top: 96px;
    display: flex; align-items: center; gap: 14px;
  }
  .brand .brand-dot { width: 22px; height: 22px; background: var(--blue); }
  .brand-name {
    font-family: "Montserrat", Arial, sans-serif; font-weight: 800;
    color: var(--blue); line-height: 1.05;
  }
  .brand-name .line-main { display: block; font-size: 40px; letter-spacing: 1px; }
  .brand-name .line-sub { display: block; font-size: 17px; letter-spacing: 9px; }

  .divider-line {
    position: absolute; left: 36px; top: 214px;
    width: 420px; height: 3px; background: var(--blue);
  }
  .phone-band {
    position: absolute; right: 0; top: 196px;
    width: 250px; height: 30px;
    background: var(--orange);
    clip-path: polygon(0 100%, 14% 0, 100% 0, 100% 100%);
    display: flex; align-items: center; justify-content: flex-end;
    padding-right: 22px; gap: 10px;
    font-family: "Montserrat", Arial, sans-serif; font-weight: 700;
    font-size: 18px; color: var(--white); letter-spacing: .5px;
  }
  .phone-band svg { width: 15px; height: 15px; }

  .person { position: absolute; left: 36px; top: 230px; }
  .person-name {
    font-family: "Montserrat", Arial, sans-serif; font-weight: 800;
    font-size: 25px; color: var(--blue); letter-spacing: .5px;
  }
  .person-role {
    font-family: "Montserrat", Arial, sans-serif; font-weight: 600;
    font-size: 15px; color: var(--orange); letter-spacing: .5px; margin-top: 2px;
  }

  .contact-list {
    position: absolute; right: 20px; top: 236px;
    list-style: none; display: flex; flex-direction: column; gap: 5px;
    align-items: flex-end;
  }
  .contact-list li {
    display: flex; align-items: center; gap: 10px;
    font-size: 14px; color: var(--ink);
  }
  .contact-list svg { width: 15px; height: 15px; flex: none; }

  .service-band {
    position: absolute; left: 0; right: 0; bottom: 0; height: 50px;
    background: var(--anthracite);
    display: flex; align-items: center; justify-content: center; gap: 12px;
    font-family: "Montserrat", Arial, sans-serif; font-weight: 700;
    font-size: 17px; color: var(--white); letter-spacing: 1.2px;
    text-transform: uppercase;
  }
  .service-band .sep { width: 10px; height: 10px; border-radius: 50%; background: var(--orange); }
</style>
</head>
<body>

  <section class="card card-back" aria-label="Card back">
    <div class="pattern-area" role="img" aria-label="Repeating tone-on-tone brand pattern on anthracite"></div>
    <div class="back-brand"><span class="brand-dot"></span>Brunnfeld Haustechnik</div>
  </section>

  <section class="card card-front" aria-label="Card front">
    <div class="brand">
      <span class="brand-dot"></span>
      <div class="brand-name">
        <span class="line-main">BRUNNFELD</span>
        <span class="line-sub">HAUSTECHNIK</span>
      </div>
    </div>

    <div class="divider-line"></div>

    <div class="phone-band">
      <span>555-240-1187</span>
      <svg viewBox="0 0 24 24" fill="#fff" aria-hidden="true"><path d="M6.6 10.8a15 15 0 0 0 6.6 6.6l2.2-2.2c.3-.3.7-.4 1-.2 1.1.4 2.3.6 3.6.6.6 0 1 .4 1 1V20c0 .6-.4 1-1 1A17 17 0 0 1 3 4c0-.6.4-1 1-1h3.5c.6 0 1 .4 1 1 0 1.3.2 2.5.6 3.6.1.3 0 .7-.2 1z"/></svg>
    </div>

    <div class="person">
      <div class="person-name">JONAS KELLER</div>
      <div class="person-role">CEO/FOUNDER</div>
    </div>

    <ul class="contact-list">
      <li>555-318-4402
        <svg viewBox="0 0 24 24" fill="none" stroke="#f7931e" stroke-width="2.2" aria-hidden="true"><rect x="6" y="2" width="12" height="20" rx="2"/><line x1="11" y1="18" x2="13" y2="18"/></svg>
      </li>
      <li>info@brunnfeldhaustechnik.com
        <svg viewBox="0 0 24 24" fill="#f7931e" aria-hidden="true"><path d="M2 5h20v14H2z"/><path d="M2 5l10 8 10-8" fill="none" stroke="#fff" stroke-width="1.6"/></svg>
      </li>
      <li>www.brunnfeldhaustechnik.com
        <svg viewBox="0 0 24 24" fill="none" stroke="#f7931e" stroke-width="2" aria-hidden="true"><circle cx="12" cy="12" r="9"/><ellipse cx="12" cy="12" rx="4" ry="9"/><line x1="3" y1="12" x2="21" y2="12"/></svg>
      </li>
    </ul>

    <div class="service-band">
      <span>Plumbing</span><span class="sep"></span>
      <span>Heating 24h Emergency Service</span><span class="sep"></span>
      <span>Maintenance</span>
    </div>
  </section>

</body>
</html>
```